Quality Monitoring Company Needs a New Site

We are an established company that has a fair number of clients but the site lacks current design standards that we'd like to keep up with. We'd like to mimic the same style of the site on quorvlinapp.example, belstrum.example, https://tindleworkpays.example/, etc. We'd also like to make sure the designer understands SEO Silos and how it effects the design elements. Attached is the structure that I'd like to follow for the pages. You don't need to design every single sub-page because they'll probably be fairly similar; however, I want to see at least 1 each. Please use the content on our current site for filler areas. Please try to do a good job of understanding what we do so you can use your best judgement on what is needed to be successful. Use our color scheme and the logo should be the side view but I included the AI just in case.
Updates

I am narrowing down on the field of designs that I have received. There are a lot of similarities between the designs I like and don't like. I'd also like to ensure that some of the inner pages get done in the next 5 days so I can see the creativity that is there as well. That is probably what is next -- getting a few inner pages completed so I can see what you can come up with (not based on our current website) because the current "front pages" are all so good and so close.

Industry/Entity Type

Telecommunications

Colors

Designer to choose colors to be used in the design.

Requirements
Must have
• SEO Silo Look and Feel
• Current Colors
Should not have
• No stockphotos whatsoever. NONE.

```html
<!DOCTYPE html>
<html lang="en">
<head>
<meta charset="utf-8">
<title>Vantelo — Call Center Quality Assurance</title>
<link rel="stylesheet" href="https://fonts.googleapis.com/css2?family=Poppins:wght@300;400;500;600;700&display=swap">
<style>
:root{
  --navy:#0c2a57;
  --blue:#1ca7ea;
  --blue-soft:#e6f4fd;
  --text:#7d8798;
  --text-dark:#3a4558;
  --bg:#f8fafd;
  --white:#ffffff;
  --line:#e3e8f0;
}
*{box-sizing:border-box;margin:0;padding:0}
html,body{width:1200px;height:4658px;overflow:hidden}
body{font-family:"Poppins",sans-serif;background:var(--bg);color:var(--text);position:relative}
.abs{position:absolute}
.page{position:relative;width:1200px;height:4658px;overflow:hidden}

/* header */
.brand{display:flex;align-items:center;gap:10px;color:var(--navy);font-weight:600;font-size:22px}
.brand-dot{width:26px;height:26px;border-radius:50%;background:var(--blue)}
.nav-link{position:absolute;top:102px;font-size:11.5px;color:var(--text-dark);text-decoration:none;white-space:nowrap}
.nav-link.active{color:var(--blue);font-weight:600}
.header-phone{left:903px;top:86px;display:flex;align-items:center;gap:10px;font-weight:600;color:var(--navy);font-size:14px}
.phone-badge{width:38px;height:38px;border-radius:50%;background:var(--blue);display:flex;align-items:center;justify-content:center}

/* type */
.hero-title{left:141px;top:300px;width:400px;font-size:21.5px;line-height:37px;font-weight:700;color:var(--navy);white-space:nowrap}
.btn{display:inline-flex;align-items:center;justify-content:center;border-radius:20px;font-size:12px;font-weight:600;letter-spacing:.5px;color:var(--white);text-transform:uppercase}
.btn-blue{background:var(--blue)}
.btn-navy{background:var(--navy)}
.section-title{width:1200px;left:0;text-align:center;font-size:36px;line-height:43px;font-weight:700;color:var(--navy)}
.section-title .light{color:var(--blue);font-weight:400}
.block-title{font-size:29px;font-weight:700;color:var(--navy)}
.block-title .light{color:var(--blue);font-weight:400}
.copy{font-size:11.5px;line-height:19.5px;color:var(--text)}
.art{border-radius:18px}

/* features */
.feature{width:320px;text-align:center}
.feature-art{width:190px;height:148px;margin:0 auto 30px;border-radius:14px;background:linear-gradient(135deg,#dcecfb,#eef4fb 60%,#d6e2f3)}
.feature h3{font-size:12.5px;letter-spacing:1.2px;font-weight:600;color:var(--navy);margin-bottom:8px}
.feature p{font-size:11.5px;line-height:19px}

/* accordion */
.acc{left:533px;width:483px;height:40px;background:var(--white);border-radius:20px;box-shadow:0 6px 18px rgba(20,50,100,.08);display:flex;align-items:center;padding:0 16px 0 8px;font-size:11px;font-weight:500;color:var(--navy)}
.acc-num{width:30px;height:30px;border-radius:50%;display:flex;align-items:center;justify-content:center;color:var(--blue);font-size:12px;margin-right:12px}
.acc.open .acc-num{background:var(--blue);color:var(--white)}
.acc-label{flex:1}

/* tabs */
.tabs{left:0;top:2283px;width:1200px;display:flex;justify-content:center;align-items:center;font-size:12.5px;color:var(--text)}
.tab{padding:0 20px;height:33px;display:flex;align-items:center;position:relative}
.tab+.tab::before{content:"";position:absolute;left:0;top:12px;height:10px;width:1px;background:var(--line)}
.tab.active{background:var(--navy);color:var(--white);border-radius:17px}
.tab.active::before,.tab.active+.tab::before{display:none}

/* blogs */
.blog{top:3619px;width:282px;height:438px;background:var(--white);box-shadow:0 8px 24px rgba(20,50,100,.07)}
.blog-art{height:212px}
.blog-body{padding:22px 18px}
.blog h4{font-size:13px;line-height:21px;font-weight:700;color:var(--navy)}
.blog time{display:block;font-size:10.5px;color:#a9b1bd;margin:6px 0 14px}
.blog p{font-size:11px;line-height:20px;letter-spacing:.2px}
.read{display:block;margin-top:14px;font-size:10.5px;font-weight:600;color:var(--blue)}

/* footer */
.footer{left:0;top:4282px;width:1200px;height:376px;background:var(--navy)}
.shout{left:211px;top:4177px;width:776px;height:209px;border-radius:105px;background:var(--blue);text-align:center}
.shout h2{font-size:43px;font-weight:400;color:var(--white);margin-top:52px;line-height:60px}
.foot-title{font-size:16px;font-weight:600;color:var(--blue)}
.foot-links{font-size:11.5px;line-height:19.8px;color:#d7e0ee}
.foot-row{display:flex;align-items:flex-start;gap:10px;font-size:12px;line-height:22px;color:#d7e0ee}
.copyright{left:0;top:4607px;width:1200px;text-align:center;font-size:11.5px;color:#c9d3e3}
</style>
</head>
<body>
<main class="page">

  <svg class="abs" style="left:0;top:0" width="1200" height="700" viewBox="0 0 1200 700" aria-hidden="true">
    <rect width="1200" height="700" fill="#f6f8fc"/>
    <path d="M700 620 C820 560 960 520 1200 500 L1200 700 L700 700 Z" fill="#eef2f9"/>
  </svg>

  <header>
    <div class="abs brand" style="left:139px;top:78px"><span class="brand-dot"></span>Vantelo</div>
    <nav>
      <a class="nav-link active" href="#" style="left:403px">Home</a>
      <a class="nav-link" href="#" style="left:463px">Services</a>
      <a class="nav-link" href="#" style="left:537px">Industries</a>
      <a class="nav-link" href="#" style="left:620px">Pricing</a>
      <a class="nav-link" href="#" style="left:683px">Team</a>
      <a class="nav-link" href="#" style="left:743px">Blog</a>
      <a class="nav-link" href="#" style="left:792px">Contact Us</a>
    </nav>
    <div class="abs header-phone">
      <span class="phone-badge">
        <svg width="16" height="16" viewBox="0 0 24 24"><path fill="#fff" d="M6.6 10.8a15.1 15.1 0 0 0 6.6 6.6l2.2-2.2c.3-.3.7-.4 1-.2 1.1.4 2.3.6 3.6.6.6 0 1 .4 1 1V20c0 .6-.4 1-1 1A17 17 0 0 1 3 4c0-.6.4-1 1-1h3.5c.6 0 1 .4 1 1 0 1.3.2 2.5.6 3.6.1.3 0 .7-.2 1z"/></svg>
      </span>800-555-0142
    </div>
  </header>

  <section class="hero">
    <h1 class="abs hero-title">We Are An Affordable, Accurate,<br>&amp; Fully Scalable Call Center<br>Quality Assurance Agency.</h1>
    <a class="abs btn btn-blue" style="left:141px;top:436px;width:154px;height:33px">Get In Touch</a>
    <div class="abs art" role="img" aria-label="Laptop displaying a quality assurance dashboard" style="left:560px;top:213px;width:550px;height:317px;background:linear-gradient(160deg,#e9eef6,#ffffff 45%,#cfd6e2)"></div>
  </section>

  <section class="services">
    <h2 class="abs section-title" style="top:723px">Our Call Center Quality<br><span class="light">Assurance Services</span></h2>
    <h3 class="abs block-title" style="left:139px;top:894px">Quality <span class="light">Assurance</span></h3>
    <p class="abs copy" style="left:139px;top:962px;width:460px">Lorem ipsum dolor sit amet, consectetuer adipiscing elit, sed diam nonummy nibh euismod tincidunt ut laoreet dolore magna aliquam erat volutpat. Ut wisi enim ad minim veniam, quis nostrud exerci tation ullamcorper suscipit lobortis nisl ut aliquip ex ea commodo consequat.</p>
    <a class="abs btn btn-navy" style="left:139px;top:1062px;width:128px;height:35px">More Info</a>
    <div class="abs art" role="img" aria-label="Team reviewing a quality dashboard with plants and clock icons" style="left:650px;top:849px;width:362px;height:308px;background:linear-gradient(135deg,#e4f1fc,#f5f8fc 55%,#dfe6f4)"></div>

    <div class="abs feature" style="left:107px;top:1234px">
      <div class="feature-art" role="img" aria-label="Coach presenting charts"></div>
      <h3>COACHING</h3>
      <p>Lorem ipsum dolor a consectetuer<br>adipiscing eldiam nonummy nibh euismod<br>tincidunt ut laoreet</p>
    </div>
    <div class="abs feature" style="left:438px;top:1234px">
      <div class="feature-art" role="img" aria-label="Team analysing sales performance"></div>
      <h3>SALES PERFORMANCE</h3>
      <p>Lorem ipsum dolor a consectetuer<br>adipiscing eldiam nonummy nibh euismod<br>tincidunt ut laoreet</p>
    </div>
    <div class="abs feature" style="left:769px;top:1234px">
      <div class="feature-art" role="img" aria-label="People working with voice analytics screens"></div>
      <h3>AI ENABLED VOICE ANALYTICS</h3>
      <p>Lorem ipsum dolor a consectetuer<br>adipiscing eldiam nonummy nibh euismod<br>tincidunt ut laoreet</p>
    </div>
  </section>

  <section class="why">
    <div class="abs art" role="img" aria-label="Call center agent with headset at a desk beside a customer" style="left:72px;top:1617px;width:452px;height:479px;background:linear-gradient(150deg,#e2effb,#f6f8fc 50%,#dbe5f2)"></div>
    <h2 class="abs block-title" style="left:535px;top:1590px;font-size:36px;line-height:47px;white-space:nowrap">Why Choose Vantelo For<br><span class="light">Your Call Center QA Needs?</span></h2>

    <div class="abs acc open" style="top:1722px">
      <span class="acc-num">01</span><span class="acc-label">We Provide Affordable &amp; Cost Effective Call Center QA Services</span>
      <svg width="18" height="2"><rect width="18" height="2" fill="#1ca7ea"/></svg>
    </div>
    <p class="abs copy" style="left:541px;top:1785px;width:450px;font-size:11px;line-height:22px">Starting at only 20c per CALL minute, we are cheaper than the latest QA technologies or hiring an internal QA team. What's more, we are just as accurate, can scale easily, and provide a full call center QA solution for you to impact positive change in your call center.</p>

    <div class="abs acc" style="top:1901px"><span class="acc-num">02</span><span class="acc-label">Our Human Analysts can Capture What QA Software Cannot</span>
      <svg width="18" height="18"><path d="M9 0v18M0 9h18" stroke="#1ca7ea" stroke-width="2"/></svg></div>
    <div class="abs acc" style="top:1968px"><span class="acc-num">03</span><span class="acc-label">We Customize Score Cards to Your Industry</span>
      <svg width="18" height="18"><path d="M9 0v18M0 9h18" stroke="#1ca7ea" stroke-width="2"/></svg></div>
    <div class="abs acc" style="top:2035px"><span class="acc-num">04</span><span class="acc-label">We'll Give You the Best View of Your Call Center</span>
      <svg width="18" height="18"><path d="M9 0v18M0 9h18" stroke="#1ca7ea" stroke-width="2"/></svg></div>
  </section>

  <section class="industries">
    <h2 class="abs section-title" style="top:2210px">Industries <span class="light">We Serve</span></h2>
    <div class="abs tabs">
      <span class="tab">Education</span><span class="tab">Insurance</span><span class="tab active">Mortgage</span><span class="tab">Automotive</span><span class="tab">Utilities</span><span class="tab">Financial Services</span><span class="tab">Home Services</span><span class="tab">Call Tracking</span>
    </div>
    <h3 class="abs block-title" style="left:186px;top:2434px;font-size:25px">Mortgage</h3>
    <p class="abs copy" style="left:186px;top:2500px;width:440px;font-size:11px;line-height:25px">Lorem ipsum dolor sit amet, consectetuer adipiscing elit, sed diam nibh laoreet euismod tincidunt ut laoreet dolore magna.</p>
    <p class="abs copy" style="left:186px;top:2560px;width:440px;font-size:11px;line-height:25px">Lorem ipsum dolor sit amet, consectetuer adipiscing elit, sed diam nonummy nibh euismod tincidunt ut laoreet dolore magna aliquam erat volutpat. Ut wisi enim ad minim veniam, quis nostrud exerci tation ullamcorper suscipit lobortis nisl ut aliquip ex ea commodo consequat. Duis autem vel eum iriure dolor in hendrerit in vulputate velit esse molestie consequat, vel illum dolore eu feugiat nulla facilisis at vero eros et accumsan.</p>
    <a class="abs btn btn-blue" style="left:186px;top:2730px;width:156px;height:33px">Call Us Today</a>
    <div class="abs" role="img" aria-label="Person reading in a chair beside a telephone with city buildings" style="left:665px;top:2364px;width:323px;height:478px;border-radius:26px;box-shadow:0 12px 30px rgba(20,50,100,.1);background:linear-gradient(170deg,#eadcf3,#e3effc 55%,#dcecfb)"></div>
  </section>

  <section class="proof">
    <div class="abs art" role="img" aria-label="Person reading on a sofa with plants, lamp and city skyline" style="left:72px;top:2972px;width:470px;height:362px;background:linear-gradient(140deg,#e9f3dc,#f4f0f6 50%,#f1dce4)"></div>
    <h2 class="abs block-title" style="left:625px;top:3025px;font-size:35px">Proof of <span class="light">Our Value</span></h2>
    <p class="abs copy" style="left:625px;top:3090px;width:420px;font-size:10.5px;line-height:20px">Organizations that have outsourced their QA program to Vantelo experienced reductions in compliance violation at a rate of 7%, increased lead conversions at a rate of 12% while improving customer retention at a rate of 9%.</p>
    <p class="abs copy" style="left:625px;top:3181px;width:420px;font-size:10.5px;line-height:20px">Call us today for a consultation on your call center's current performance and ideas how to get better performance from your team.</p>
    <div class="abs" style="left:625px;top:3240px;display:flex;align-items:center;gap:12px;font-size:11.5px;font-weight:600;color:var(--navy)">
      <svg width="22" height="18" viewBox="0 0 22 18"><rect width="22" height="18" rx="3" fill="#1ca7ea"/><path d="M8 5l7 4-7 4z" fill="#fff"/></svg>Watch Video
    </div>
  </section>

  <section class="blogs">
    <h2 class="abs section-title" style="top:3538px">Featured <span class="light">Blogs</span></h2>
    <article class="abs blog" style="left:139px">
      <div class="blog-art" role="img" aria-label="Silhouettes of managers with growth charts" style="background:linear-gradient(135deg,#c6d6ee,#3d5f9a)"></div>
      <div class="blog-body"><h4>11 Great Call Center Supervisor Skills</h4><time>October 23, 2019</time>
      <p>If you have read our article, Important Call Center Skills For Agents, you may be wondering about the call center supervisor skills that are necessary.</p><span class="read">READ MORE</span></div>
    </article>
    <article class="abs blog" style="left:457px">
      <div class="blog-art" role="img" aria-label="Call center agent on the phone at a desk" style="background:linear-gradient(135deg,#8a8f97,#2f3338)"></div>
      <div class="blog-body"><h4>7 Important Call Center Skills For Agents</h4><time>October 21, 2019</time>
      <p>Call center agents are a little bit like superheroes. They have to solve problems, deal with difficult people, and still do their job correctly. There are some vital</p><span class="read">READ MORE</span></div>
    </article>
    <article class="abs blog" style="left:775px">
      <div class="blog-art" role="img" aria-label="Hand drawing a process flowchart" style="background:linear-gradient(135deg,#e8ebf0,#b9c0cc)"></div>
      <div class="blog-body"><h4>Process vs. Product | Easy Solution</h4><time>October 19, 2019</time>
      <p>There have been a lot of questions asking about Process vs. Product in call centers. In this article, we are going to try and answer your questions related to the</p><span class="read">READ MORE</span></div>
    </article>
  </section>

  <footer>
    <div class="abs footer"></div>
    <div class="abs shout">
      <h2>Give Us A Shout</h2>
      <a class="btn btn-navy" style="width:156px;height:35px;margin-top:6px;font-weight:500">Get In Touch</a>
    </div>

    <h4 class="abs foot-title" style="left:139px;top:4442px">Quick Links</h4>
    <div class="abs foot-links" style="left:139px;top:4478px">Home<br>Services<br>System Details<br>Pricing</div>
    <div class="abs foot-links" style="left:295px;top:4478px">Team<br>Blog<br>Contact Us<br>Login</div>

    <h4 class="abs foot-title" style="left:461px;top:4442px">Contact Us</h4>
    <div class="abs foot-row" style="left:463px;top:4478px">
      <svg width="11" height="15" viewBox="0 0 12 16" style="margin-top:4px"><path d="M6 0a6 6 0 0 0-6 6c0 4.5 6 10 6 10s6-5.5 6-10a6 6 0 0 0-6-6zm0 8.5A2.5 2.5 0 1 1 6 3.5a2.5 2.5 0 0 1 0 5z" fill="#fff"/></svg>
      <span>2210 Harbor Lane,<br>&nbsp;&nbsp;Riverton, CA 90210</span>
    </div>
    <div class="abs foot-row" style="left:660px;top:4478px">
      <svg width="13" height="13" viewBox="0 0 24 24" style="margin-top:5px"><path fill="#fff" d="M6.6 10.8a15.1 15.1 0 0 0 6.6 6.6l2.2-2.2c.3-.3.7-.4 1-.2 1.1.4 2.3.6 3.6.6.6 0 1 .4 1 1V20c0 .6-.4 1-1 1A17 17 0 0 1 3 4c0-.6.4-1 1-1h3.5c.6 0 1 .4 1 1 0 1.3.2 2.5.6 3.6.1.3 0 .7-.2 1z"/></svg>
      <span>800-555-0142</span>
    </div>
    <div class="abs foot-row" style="left:660px;top:4514px">
      <svg width="13" height="11" viewBox="0 0 16 12" style="margin-top:6px"><rect width="16" height="12" rx="1.5" fill="#fff"/><path d="M1 1l7 6 7-6" stroke="#0c2a57" stroke-width="1.5" fill="none"/></svg>
      <span>hello@vantelo.example</span>
    </div>

    <div class="abs brand" style="left:922px;top:4474px;color:var(--white);font-size:28px"><span class="brand-dot" style="width:34px;height:34px"></span>Vantelo</div>

    <p class="abs copyright">Copyright © 2019 VANTELO. All Rights Reserved.</p>
  </footer>
</main>
</body>
</html>
```